****Business Card Design for Cormorant Ridge. Design based around attached logo/company name

I’m looking for business card design for my company Cormorant Ridge Holdings,LLC. Design should be professional, sharp and minimal. Outside of the attached logos, greyscale colors for remainder of cards. My thoughts are two-sided card with attached logo on one side and my info on the other but open to one-sided as well with right design.
Target Market(s)
Real estate professionals including banks, private investors, property owners, developers, commercial tenants like Brewloft, Grocana or Tandberry’s.
Industry/Entity Type
Commercial real estate development and investments.
Contact Information for Business Card
Name, title, email, phone #’s, web address and physical address
Font styles to use
Other font styles liked:
- Helvetica, Garamond, etc
Colors
Designer to choose only greyscale colors for use in the design.
Requirements
Must have
- Attached logo first or second options.
Nice to have
- Two sided card with logo on one side. Attached Logo/company name can be laid out any way that flows as long as it’s legible.name
Should not have
- No loud colors. ***Please do not include logo, I have removed the company design with a logo image.

```html
<!DOCTYPE html>
<html lang="en">
<head>
<meta charset="UTF-8">
<title>Cormorant Ridge Holdings – Business Card</title>
<link href="https://fonts.googleapis.com/css2?family=EB+Garamond:wght@400&family=Arimo:wght@400&display=swap" rel="stylesheet">
<style>
  :root {
    --page: #e9eaeb;
    --card-light: #6f7686;
    --card-dark: #535a6a;
    --ink: #f3f4f6;
    --ink-soft: #e4e6ea;
    --rule: rgba(240, 242, 246, 0.55);
  }
  * { margin: 0; padding: 0; box-sizing: border-box; }
  html, body {
    width: 1200px;
    height: 1200px;
    overflow: hidden;
    background: var(--page);
  }
  .canvas {
    position: relative;
    width: 1200px;
    height: 1200px;
  }
  .card {
    position: absolute;
    left: 262px;
    width: 686px;
    height: 391px;
    background: linear-gradient(200deg, var(--card-light) 0%, var(--card-dark) 100%);
    color: var(--ink);
  }
  .card--front { top: 165px; }
  .card--back { top: 626px; }

  .wordmark {
    position: absolute;
    text-align: center;
    font-family: "EB Garamond", Garamond, serif;
    font-weight: 400;
    color: var(--ink);
    text-transform: uppercase;
    line-height: 1.1;
  }
  .card--front .wordmark {
    left: 100px;
    top: 168px;
    width: 232px;
    font-size: 20px;
    letter-spacing: 1.5px;
  }
  .card--front .wordmark .wordmark__sub {
    font-size: 11px;
    letter-spacing: 1.6px;
  }
  .card--back .wordmark {
    left: 0;
    top: 148px;
    width: 686px;
    font-size: 42px;
    letter-spacing: 3px;
  }
  .card--back .wordmark .wordmark__sub {
    font-size: 19px;
    letter-spacing: 3px;
    margin-top: 6px;
  }
  .wordmark__sub { display: block; }

  .divider {
    position: absolute;
    left: 350px;
    top: 122px;
    width: 1px;
    height: 141px;
    background: var(--rule);
  }

  .contact {
    position: absolute;
    left: 372px;
    top: 104px;
    font-family: Arimo, Helvetica, Arial, sans-serif;
    font-size: 15px;
    line-height: 19px;
    color: var(--ink-soft);
  }
  .contact__name {
    font-family: "EB Garamond", Garamond, serif;
    font-size: 22px;
    line-height: 26px;
    letter-spacing: 0.5px;
    color: var(--ink);
    text-transform: uppercase;
  }
  .contact__title { margin-bottom: 14px; }
  .contact__address { margin-bottom: 14px; }
  .contact__lines { padding-left: 3px; }
</style>
</head>
<body>
<main class="canvas">
  <section class="card card--front" aria-label="Card front with contact details">
    <div class="wordmark">
      Cormorant Ridge
      <span class="wordmark__sub">Holdings, LLC</span>
    </div>
    <div class="divider"></div>
    <div class="contact">
      <div class="contact__name">Daniel Hartwell</div>
      <div class="contact__title">President</div>
      <div class="contact__address">
        4120 Alder Crest Way<br>
        Juneau, Alaska 34681
      </div>
      <div class="contact__lines">
        369-480-2173<br>
        info@cormorantridge.com<br>
        www.cormorantridge.com
      </div>
    </div>
  </section>

  <section class="card card--back" aria-label="Card back with company name">
    <div class="wordmark">
      Cormorant Ridge
      <span class="wordmark__sub">Holdings, LLC</span>
    </div>
  </section>
</main>
</body>
</html>
```